Business Card Design Project

Looking for a simple and stylish business card. We are an Advertising Company. The card Must feature the company logo (attached) and also this info.
p: 0461528390
e: sales@jh-promo.com.au
w: www.jh-promo.com.au
We Advertise mainly using TV screens featured in restaurants and cafe. See website for more about the business.
Not really looking for a plain background, but at the same time do not want to much happening in the Background. I am not really to fussy though with the design or the colour scheme, and I am leaving the creativity part up to you creative designers.
Business

```html
<!DOCTYPE html>
<html lang="en">
<head>
<meta charset="utf-8">
<title>JH Promo Business Card</title>
<link href="https://fonts.googleapis.com/css2?family=Questrial&display=swap" rel="stylesheet">
<style>
  :root {
    --backdrop: #e4e2df;
    --card: #ffffff;
    --ink: #2b2b2b;
    --ink-soft: #555555;
    --brand: #2a5bb8;
    --accent-start: #3a6fc4;
    --accent-end: #b95aa8;
  }
  * { margin: 0; padding: 0; box-sizing: border-box; }
  html, body { width: 1200px; height: 576px; overflow: hidden; }
  body {
    background: var(--backdrop);
    font-family: "Questrial", "Century Gothic", sans-serif;
    color: var(--ink);
    display: flex;
    align-items: center;
    justify-content: center;
    gap: 120px;
  }
  .card {
    position: relative;
    width: 300px;
    height: 520px;
    background: var(--card);
    box-shadow: 0 6px 18px rgba(0,0,0,0.18);
    overflow: hidden;
  }
  .accent-band {
    position: absolute;
    left: 0; right: 0;
    height: 62px;
    background: linear-gradient(90deg, var(--accent-start), var(--accent-end));
  }
  .card--front .accent-band { bottom: 0; }
  .card--back .accent-band { top: 0; }

  .brand {
    position: absolute;
    top: 58px; left: 34px;
    display: flex;
    align-items: center;
    gap: 12px;
  }
  .brand-mark {
    width: 30px; height: 30px;
    background: var(--brand);
  }
  .brand-name {
    font-size: 34px;
    letter-spacing: 1px;
    color: var(--brand);
  }
  .person {
    position: absolute;
    left: 34px;
  }
  .card--front .person { top: 190px; }
  .card--back .person { top: 150px; }
  .person-name { font-size: 27px; line-height: 1.1; }
  .person-title { font-size: 13px; color: var(--ink-soft); margin-top: 4px; }
  .person-phone { font-size: 25px; margin-top: 20px; letter-spacing: 1px; }
  .contacts {
    position: absolute;
    left: 34px;
    font-size: 14px;
    line-height: 1.6;
    color: var(--ink);
  }
  .card--front .contacts { bottom: 86px; }
  .card--back .contacts { bottom: 40px; }
  .contacts b { font-weight: 700; margin-right: 4px; }
</style>
</head>
<body>
  <article class="card card--front">
    <div class="brand">
      <span class="brand-mark"></span>
      <span class="brand-name">JH PROMO</span>
    </div>
    <div class="person">
      <p class="person-name">Daniel Merrow</p>
      <p class="person-title">Managing Director</p>
      <p class="person-phone">0461528390</p>
    </div>
    <div class="contacts">
      <p><b>e:</b>sales@jh-promo.com.au</p>
      <p><b>w:</b>www.jh-promo.com.au</p>
    </div>
    <div class="accent-band" role="img" aria-label="Decorative multicolour stripe band"></div>
  </article>

  <article class="card card--back">
    <div class="accent-band" role="img" aria-label="Decorative multicolour stripe band"></div>
    <div class="person">
      <p class="person-name">Daniel Merrow</p>
      <p class="person-title">Managing Director</p>
      <p class="person-phone">0461528390</p>
    </div>
    <div class="contacts">
      <p><b>e:</b>sales@jh-promo.com.au</p>
      <p><b>w:</b>www.jh-promo.com.au</p>
    </div>
  </article>
</body>
</html>
```